Harbor Lawn and Stoneworks Flyer/Brochure

Flyer/Brochure for artificial turf and paver company. Photos and txt<br/>Specializes in Turf, Pavers, Patio, Decorative Rock, Hardscape, Landscape Design.

Target Market(s)

Homeowners

Industry/Entity Type

Construction

Font styles to use
Sans Serif

Colors
9bcb3c

Requirements
Must have
• Photos, we will provide as well as logo
• phone number and email address
• similar branding as website
• www.harborlsw.com
Nice to have
• eye catching not too busy
• clean and easy to read
• Hi! Please see photos on our instagram - there are a couple shots that may be better than the website there.
• Also, photo of dog on turf. Please mention kid -play turf and pet turf is available or something like "your pup will love our pet turf"
• Add- "Ask us about our specials"
• phone number is 800-413-2786

```html
<!DOCTYPE html>
<html lang="en">
<head>
<meta charset="utf-8">
<title>Harbor Lawn and Stoneworks Flyer</title>
<link href="https://fonts.googleapis.com/css2?family=Montserrat:wght@300;400;500;600;700;800&family=Roboto:wght@700;900&display=swap" rel="stylesheet">
<style>
  :root {
    --green: #6cb52d;
    --green-bright: #9bcb3c;
    --ink: #2b2b2b;
    --panel: #ebebeb;
    --bar: #333230;
    --page: #d9d9d9;
    --white: #ffffff;
  }
  * { margin: 0; padding: 0; box-sizing: border-box; }
  html, body { width: 703px; height: 1200px; overflow: hidden; background: var(--page); }
  body { font-family: "Montserrat", sans-serif; color: var(--ink); }
  .flyer {
    position: absolute; left: 0; top: 103px;
    width: 703px; height: 993px;
    background: var(--white); overflow: hidden;
    box-shadow: 0 6px 18px rgba(0,0,0,.25);
  }
  .flyer-art { position: absolute; inset: 0; }
  .headline {
    position: absolute; left: 57px; top: 62px;
    color: var(--white); line-height: 1.06;
  }
  .headline .lead { font-family: "Montserrat", sans-serif; font-weight: 300; font-size: 42px; letter-spacing: 1px; }
  .headline .strong { font-family: "Roboto", sans-serif; font-weight: 900; font-size: 44px; display: block; }
  .brand-name {
    position: absolute; left: 20px; top: 325px; width: 390px;
    text-align: center; font-weight: 800; font-size: 25px; line-height: 1.15;
    color: var(--ink); letter-spacing: .5px; text-transform: uppercase;
  }
  .guarantee { position: absolute; left: 52px; top: 466px; width: 300px; }
  .guarantee h2 { color: var(--green); font-weight: 800; font-size: 18px; line-height: 1.3; }
  .guarantee p { font-size: 10.6px; line-height: 12.8px; margin-top: 9px; text-align: left; }
  .service p { font-size: 10.6px; line-height: 12.8px; text-align: justify; }
  .service { position: absolute; }
  .service h3 {
    display: flex; align-items: center; gap: 8px;
    color: var(--green); font-weight: 700; font-size: 18px; letter-spacing: .2px;
  }
  .service h3 svg { width: 30px; height: 30px; flex: none; }
  .service p { margin-top: 5px; }
  .service--pavers { left: 54px; top: 622px; width: 265px; }
  .service--turf { left: 397px; top: 622px; width: 265px; }
  .service--patio { left: 54px; top: 746px; width: 608px; }
  .service--patio p { margin-top: 4px; }
  .contact {
    position: absolute; left: 0; top: 945px; width: 703px; height: 48px;
    display: flex; align-items: center; color: var(--white);
  }
  .contact .call { margin-left: 62px; font-size: 19px; font-weight: 400; letter-spacing: .3px; }
  .contact .call strong { font-weight: 600; font-size: 22px; margin-left: 4px; }
  .contact .web { margin-left: 55px; font-size: 18px; display: flex; align-items: center; gap: 8px; }
  .contact .web svg { width: 16px; height: 16px; }
</style>
</head>
<body>
<main class="flyer">
  <svg class="flyer-art" viewBox="0 0 703 993" width="703" height="993">
    <defs>
      <linearGradient id="heroTone" x1="0" y1="0" x2="1" y2="1">
        <stop offset="0" stop-color="#3b4630"/>
        <stop offset=".45" stop-color="#55703a"/>
        <stop offset="1" stop-color="#5f9a3a"/>
      </linearGradient>
      <linearGradient id="paverTone" x1="0" y1="0" x2="1" y2="1">
        <stop offset="0" stop-color="#8c9198"/><stop offset="1" stop-color="#5d636b"/>
      </linearGradient>
      <linearGradient id="poolTone" x1="0" y1="0" x2="0" y2="1">
        <stop offset="0" stop-color="#b9cfe3"/><stop offset=".5" stop-color="#5fb7c9"/><stop offset="1" stop-color="#3f8a2c"/>
      </linearGradient>
      <linearGradient id="patioTone" x1="0" y1="0" x2="0" y2="1">
        <stop offset="0" stop-color="#6f9fd6"/><stop offset=".5" stop-color="#d8d2c6"/><stop offset="1" stop-color="#4f7a36"/>
      </linearGradient>
    </defs>

    <rect class="hero-photo" x="0" y="0" width="703" height="420" fill="url(#heroTone)" role="img" aria-label="Backyard with synthetic turf putting green and landscaping"/>
    <rect x="0" y="380" width="703" height="613" fill="var(--white)"/>
    <ellipse cx="213" cy="358" rx="225" ry="78" fill="var(--white)" stroke="var(--green)" stroke-width="6"/>

    <circle cx="608" cy="399" r="95" fill="url(#poolTone)" stroke="var(--white)" stroke-width="4" role="img" aria-label="Pool surrounded by turf and palms"/>
    <circle cx="467" cy="299" r="102" fill="url(#paverTone)" stroke="var(--white)" stroke-width="4" role="img" aria-label="Close view of grey paver stones"/>
    <circle cx="472" cy="449" r="102" fill="url(#patioTone)" stroke="var(--white)" stroke-width="4" role="img" aria-label="House with white patio cover and garden"/>

    <rect x="0" y="605" width="703" height="305" fill="var(--panel)"/>

    <path d="M0 896 C 40 930, 80 938, 160 940 L 703 940 L 703 993 L 0 993 Z" fill="var(--green-bright)"/>
    <path d="M0 945 L 650 945 C 680 948, 695 965, 703 985 L 703 993 L 0 993 Z" fill="var(--bar)"/>
  </svg>

  <h1 class="headline">
    <span class="lead">MAKE YOUR</span>
    <span class="strong">OUTDOOR LIVING</span>
    <span class="strong">DREAM A REALITY</span>
  </h1>

  <div class="brand-name">Harbor Lawn<br>and Stoneworks</div>

  <section class="guarantee">
    <h2>We Guarantee<br>Your Satisfaction!</h2>
    <p>With long-time ties to the community, Harbor Lawn and Stoneworks is committed to being here before, during and after you purchase a new product or service from us. As licensed, bonded, and insured contractors, you can rest easy when having us do work for you!</p>
  </section>

  <section class="service service--pavers">
    <h3>
      <svg viewBox="0 0 30 30"><g fill="none" stroke="var(--green)" stroke-width="2"><path d="M4 8 L14 4 L26 6 L26 26 L14 27 L4 24 Z"/><path d="M14 4 V27 M4 16 L14 17 L26 15 M9 6 V25 M20 5 V26"/></g></svg>
      PAVER SYSTEMS
    </h3>
    <p>The perfect solution if you are looking for a customized hardscape design option that adds tons of curb appeal, is much stronger and more durable than traditional wood decking and is virtually maintenance free.</p>
  </section>

  <section class="service service--turf">
    <h3>
      <svg viewBox="0 0 30 30"><g fill="none" stroke="var(--green)" stroke-width="2" stroke-linecap="round"><path d="M3 26 H27"/><path d="M6 26 L4 12 M10 26 L9 8 M14 26 L15 5 M18 26 L20 9 M22 26 L26 13"/></g></svg>
      SYNTHETIC TURF
    </h3>
    <p>Today's synthetic turf is remarkably versatile replicating the lush beauty of the finest cared for lawns and is sure to be the envy of your neighbors. Whether you're interested in backyards or playgrounds or simply want to install that often dreamt-about putting green</p>
  </section>

  <section class="service service--patio">
    <h3>
      <svg viewBox="0 0 30 30"><g fill="none" stroke="var(--green)" stroke-width="2"><path d="M3 10 L15 3 L27 10 Z"/><path d="M5 10 V27 M25 10 V27 M3 27 H27 M10 14 H20 V22 H10 Z M15 14 V22"/></g></svg>
      PATIO COVERS
    </h3>
    <p>What have you always dreamed about...an outdoor kitchen, a fire pit, a vine covered pergola to entertain family and friends? Let Harbor Lawn and Stoneworks make those dreams a reality with a custom built patio cover. We work with a variety of materials and timeless finishes to create stunning outdoor structures built to make a lasting impression. Our patio covers are made for relaxation and enjoyment! Lattice or solid, they are constructed of durable materials that are maintenance free and can include ceiling fans, lighting and your choice of colors. The attractive design blends seamlessly with neighboring structures yet still provides elemental protection. Outstanding weather and the California lifestyle are the envy of the world. Why not revel in your new backyard and celebrate the good life!</p>
  </section>

  <footer class="contact">
    <span class="call">CALL US NOW: <strong>800-413-2786</strong></span>
    <span class="web">
      <svg viewBox="0 0 16 16"><g fill="none" stroke="var(--green-bright)" stroke-width="1.5"><circle cx="8" cy="8" r="6.5"/><path d="M1.5 8 H14.5 M8 1.5 C4.5 5, 4.5 11, 8 14.5 M8 1.5 C11.5 5, 11.5 11, 8 14.5"/></g></svg>
      www.harborlsw.com
    </span>
  </footer>
</main>
</body>
</html>
```